AI Layout work for Business Cards, Letterhead and Compliment Slip for Award-winning UK Property Deve

No actual logo or corporate identity design work needed here but some skill required to create layouts for business card, letterhead and compliment slip for this award-winning company.
I can provide AI files featuring the company logo and an initial layout of the business card, (6 versions featuring the same design but for different personnel), along with some initial instructions (with possibly more to follow from the client). The finished layouts for each item need to be print-ready in AI format - 8 in all (6 for each business card plus 1 for letterhead and 1 for compliment slip).
I've given this project a 5-day duration but there may be some flexibility built into that depending on client feedback. Hopefully that won't be a problem.
UPDATE:
The client has been very prescriptive about the layout and design of these. To that end, please find 3 additional pdfs that explain what's required.
1.
All BUSINESS CARDS need to be laid out as per the attached AI file (but see latest pdf to check which layout - there are 2 in the original AI file). Use the details in the RUNE-contact-details.pdf to create 6 individual AI files, one for each card.
2.
Create 2 additional AI files, one each for the LETTERHEAD and the COMPLIMENT SLIP based on the latest mock-up that I've provided (letterhead-layout-final.pdf)
In all, I need EIGHT individual AI files, 6 for each business card, 1 for the letterhead and 1 for the compliment slip. I'd like to get this done as soon as possible now please.
Target Market(s)
Purchasers of upmarket luxury properties - see here: http://www.runeestates.co.uk
Industry/Entity Type
Business
Requirements
Must have
- Layouts need to be cool, understated and uncluttered.
Nice to have
- Please keep it simple! The actual logo background colour is likely to change (awaiting confirmation from client) but accompanying text detail and font (Deja Vu Sans Condensed) can remain as seen in the files below - for the time being at least! That having been said, I'm open to suggestions.
Should not have
- Nothing extreme or ostentatious please.

```html
<!DOCTYPE html>
<html lang="en">
<head>
<meta charset="utf-8">
<title>RUNE Compliment Slip</title>
<link href="https://fonts.googleapis.com/css2?family=Lato:wght@300;700&family=Cormorant+Garamond:wght@500&display=swap" rel="stylesheet">
<style>
  :root {
    --navy: #020b5a;
    --accent-deep: #2b3a8a;
    --accent-mid: #6a82b6;
    --accent-pale: #d3dde9;
    --paper: #ffffff;
    --frame: #111111;
  }
  * { margin: 0; padding: 0; box-sizing: border-box; }
  html, body {
    width: 1200px; height: 1000px; overflow: hidden;
    background: var(--paper);
  }
  .canvas { position: relative; width: 1200px; height: 1000px; }
  .slip {
    position: absolute; left: 33px; top: 235px;
    width: 1146px; height: 540px;
    border: 1.5px solid var(--frame);
    border-radius: 2px;
    background: var(--paper);
    overflow: hidden;
  }
  .brand-block {
    position: absolute; left: 0; top: 0;
    width: 270px; height: 174px;
    background: var(--navy);
    display: flex; align-items: center; justify-content: center;
  }
  .brand-name {
    font-family: "Cormorant Garamond", serif;
    font-weight: 500;
    font-size: 82px;
    letter-spacing: 2px;
    color: var(--paper);
  }
  .corner-motif {
    position: absolute; left: 841px; top: 4px;
    width: 298px; height: 148px;
    background: linear-gradient(180deg, var(--accent-deep) 0%, var(--accent-mid) 50%, var(--accent-pale) 100%);
  }
  .contact-band {
    position: absolute; left: 0; bottom: 0;
    width: 100%; height: 137px;
    background: var(--navy);
    color: var(--paper);
    font-family: "Lato", sans-serif;
    text-align: center;
  }
  .contact-line {
    position: absolute; left: 0; right: 0; top: 39px;
    font-weight: 700; font-size: 22px; line-height: 28px;
  }
  .address-line {
    position: absolute; left: 0; right: 34px; top: 79px;
    font-weight: 300; font-size: 20.5px; line-height: 26px;
  }
</style>
</head>
<body>
<div class="canvas">
  <div class="slip">
    <div class="brand-block">
      <span class="brand-name">RUNE</span>
    </div>

    <div class="corner-motif" role="img" aria-label="Decorative pattern of overlapping blue squares"></div>

    <div class="contact-band">
      <p class="contact-line">TEL: +44 (0)1632 960418 | WEB:&nbsp; www.runeestates.co.uk | EMAIL: enquiries@runeestates.co.uk</p>
      <p class="address-line">RUNE Exclusive Estates - Brook Mill House, Brook Mill Lane, Ashcombe Vale, AV3 7QR</p>
    </div>
  </div>
</div>
</body>
</html>
```